Petal Sprite - web design for my new flower atelier

I would like to ask for design proposal for my newly established flower atelier. My brand name is Petal Sprite and I focus on realisation of events and flower projects (any kind) for physical as well as legel persons. I don’t operate as a standard flowershop. I would like to have 5 key parts - 1/Landing pg/welcome, 2/About me, 3/Gallery, 4/References, 5/Contact details. I would like the web design to reflect the way I am/ I do the things, ie, be slightly different, do non-tradiotional arrangements, my passion for flowers, gentle& fregile style, love for minimalism and details in the arrangements. I attach couple of photos of what I do so that you can better understand my style . You can see more on IG mirka_petal_sprite or FB Petal Sprite. I was wondering maybe one of the first 2 photos could be part of the landing pg. Or another idea is to have a design similar to this one https://thistlebloomstudio.example, ie to choose 3-5photos which are being animated like here. However, I am open to discuss any ideas and look forward for all the proposals.

Target Market(s)

physical as well as legal persons - weddings, celebrations, business events, projects for hotels, beaty salons, restaurants and others.. actually any kind of flower project

Industry/Entity Type

flowers

Number of Pages Required

1 page

Font styles to use
Other font styles liked:
• the font which matches the logo font style

Requirements
Must have
• to reflect the way I am as described above, I prefer more simple way of design, with the attention to a detail, I prefer pastel colours

```html
<!DOCTYPE html>
<html lang="en">
<head>
<meta charset="utf-8">
<title>Petal Sprite – Flower Atelier</title>
<link rel="stylesheet" href="https://fonts.googleapis.com/css2?family=Great+Vibes&family=Poppins:wght@400;500;600;700&display=swap">
<style>
:root{
  --brown:#86693f;
  --brown-dark:#6f5532;
  --cream:#f3eee6;
  --mist:#f4f2ef;
  --ink:#111111;
  --text:#333333;
  --white:#ffffff;
  --black:#000000;
}
*{margin:0;padding:0;box-sizing:border-box}
html,body{width:1200px;height:3706px;overflow:hidden}
body{position:relative;background:var(--white);font-family:'Poppins',sans-serif;color:var(--text)}
.abs{position:absolute}
.script{font-family:'Great Vibes',cursive;font-weight:400;color:var(--brown)}
.heading{font-family:'Poppins',sans-serif;font-weight:700;color:var(--ink);line-height:1}
.bar{position:absolute;height:3px;background:var(--brown);width:50px}
.btn{position:absolute;display:flex;align-items:center;justify-content:center;border-radius:24px;font-weight:600;font-size:15px;background:var(--brown);color:var(--white)}
.photo{position:absolute}

/* top bar */
.topbar{left:0;top:0;width:1200px;height:33px;background:var(--brown);color:var(--white);font-size:12px}
.topbar span{position:absolute;top:9px}
.topbar .sep{width:1px;height:22px;top:5px;background:rgba(255,255,255,.6)}
.topbar .dot{width:9px;height:9px;border-radius:50%;background:var(--white);top:12px}
.navbar{left:0;top:33px;width:1200px;height:56px;background:var(--white);box-shadow:0 1px 4px rgba(0,0,0,.08)}
.nav a{position:absolute;top:58px;font-size:12px;font-weight:500;color:var(--ink);text-decoration:none}
.nav a.active{border-bottom:1px solid var(--ink)}
.logo-badge{left:130px;top:0;width:120px;height:120px;border-radius:50%;background:var(--white);box-shadow:0 2px 6px rgba(0,0,0,.15);display:flex;align-items:center;justify-content:center;font-size:16px;color:var(--brown);font-weight:500}

/* hero */
.hero-bg{left:0;top:89px}
.hero-text{left:132px;color:var(--white)}
.hero p{position:absolute;left:132px;top:372px;width:470px;font-size:13px;line-height:27px;color:var(--white)}
.get-started{left:131px;top:468px;width:173px;height:46px;background:var(--white);color:var(--brown)}

/* about */
.about p{position:absolute;left:619px;top:958px;width:468px;font-size:11.2px;line-height:24px;text-align:justify;color:var(--text)}

/* references */
.refs p{position:absolute;left:170px;top:1606px;width:860px;font-size:11.4px;line-height:24px;text-align:center;color:var(--text)}

/* contact */
.contact-bg{left:0;top:2727px;width:1200px;height:700px;background:var(--mist)}
.info-item{position:absolute;left:190px;font-size:16px;line-height:28px;color:var(--ink)}
.social-sq{position:absolute;top:3128px;width:24px;height:24px;border-radius:3px}
.field{position:absolute;background:var(--white);border:1px solid #e6e2dc;font-size:11px;color:#666;padding:15px 18px}

/* footer */
.footer h4{position:absolute;top:3400px;font-size:13px;font-weight:700;color:var(--white);letter-spacing:.2px}
.footer ul{list-style:none}
.footer li{position:absolute;list-style:none;font-size:13px;color:var(--white)}
.footer .chev{display:inline-block;width:16px;font-size:13px}
.foot-line{left:52px;top:3600px;width:1094px;height:1px;background:#555}
.copy{left:0;top:3618px;width:1200px;text-align:center;font-size:13px;color:var(--white)}
.foot-circle{position:absolute;top:3648px;width:28px;height:28px;border-radius:50%;background:var(--brown)}
</style>
</head>
<body>

<!-- top bar -->
<div class="abs topbar">
  <span style="left:476px">
    <svg width="11" height="11" viewBox="0 0 24 24" style="vertical-align:-1px"><path fill="#fff" d="M6.6 10.8a15 15 0 0 0 6.6 6.6l2.2-2.2c.3-.3.7-.4 1-.2 1.1.4 2.3.6 3.6.6.6 0 1 .4 1 1V20c0 .6-.4 1-1 1A17 17 0 0 1 3 4c0-.6.4-1 1-1h3.5c.6 0 1 .4 1 1 0 1.2.2 2.4.6 3.6.1.3 0 .7-.2 1z"/></svg>
    +1 555 014 2290</span>
  <span class="sep" style="left:620px"></span>
  <span style="left:660px">
    <svg width="12" height="10" viewBox="0 0 24 18" style="vertical-align:-1px"><path fill="#fff" d="M0 0h24v2L12 10 0 2zM0 4l12 8 12-8v14H0z"/></svg>
    hello@petalsprite.example</span>
  <span class="sep" style="left:860px"></span>
  <span style="left:888px">
    <svg width="11" height="11" viewBox="0 0 24 24" style="vertical-align:-1px"><path fill="#fff" d="M10 4l8 8-8 8v-5H2V9h8zM14 2h8v20h-8v-2h6V4h-6z"/></svg>
    Login</span>
  <span class="sep" style="left:964px"></span>
  <span class="dot" style="left:999px"></span>
  <span class="dot" style="left:1016px"></span>
  <span class="dot" style="left:1033px"></span>
  <span class="dot" style="left:1050px"></span>
</div>
<div class="abs navbar"></div>
<nav class="nav">
  <a class="active" style="left:619px">HOME</a>
  <a style="left:689px">ABOUT ME</a>
  <a style="left:787px">GALLERY</a>
  <a style="left:875px">REFERENCES</a>
  <a style="left:986px">CONTACT ME</a>
</nav>
<div class="abs logo-badge">Petal Sprite</div>

<!-- hero -->
<section class="hero">
  <svg class="abs hero-bg" width="1200" height="720" viewBox="0 89 1200 720" role="img" aria-label="Faded photo of potted flowers against a brick wall under a brown tint">
    <defs>
      <linearGradient id="heroTone" x1="0" y1="0" x2="1" y2="1">
        <stop offset="0" stop-color="#8e7449"/>
        <stop offset="1" stop-color="#7a603b"/>
      </linearGradient>
    </defs>
    <path d="M0 89H1200V626Q600 700 0 626Z" fill="url(#heroTone)"/>
    <path d="M0 660Q600 826 1200 660" fill="none" stroke="#86693f" stroke-width="5"/>
    <circle cx="578" cy="695" r="5" fill="#fff" stroke="#555" stroke-width="1.2"/>
    <circle cx="592" cy="695" r="4.5" fill="#fff" stroke="#555" stroke-width="1"/>
    <circle cx="606" cy="695" r="4.5" fill="#fff" stroke="#555" stroke-width="1"/>
    <circle cx="620" cy="695" r="4.5" fill="#fff" stroke="#555" stroke-width="1"/>
  </svg>
  <div class="abs hero-text script" style="top:228px;font-size:50px;color:var(--white)">Welcome To</div>
  <div class="abs hero-text heading" style="top:280px;font-size:70px;color:var(--white)">Petal Sprite</div>
  <p>Lorem ipsum dolor sit amet, consectetur adipiscing elit, sed do eiusmod tempor incididunt ut labore et dolore magna aliqua. Quis ipsum sus­pendisse ultrices gravida.</p>
  <div class="btn get-started">Get Started</div>
  <svg class="photo" style="left:600px;top:168px" width="470" height="460" viewBox="0 0 470 460">
    <defs>
      <radialGradient id="heroPhoto" cx=".5" cy=".45" r=".6">
        <stop offset="0" stop-color="#c9b79a"/>
        <stop offset=".55" stop-color="#8a9366"/>
        <stop offset="1" stop-color="#c7c3bc"/>
      </radialGradient>
    </defs>
    <circle cx="235" cy="223" r="219" fill="url(#heroPhoto)" role="img" aria-label="Photo of an orange and cream flower arrangement in a white vase"/>
    <path d="M330 13A232 232 0 0 1 190 450" fill="none" stroke="#fff" stroke-width="5" stroke-linecap="round"/>
    <path d="M5 238A232 232 0 0 0 160 441" fill="none" stroke="#fff" stroke-width="3" stroke-linecap="round"/>
  </svg>
</section>

<!-- about -->
<section class="about">
  <div class="abs" role="img" aria-label="Flower line drawing behind the portrait" style="left:0;top:760px;width:560px;height:600px;background:radial-gradient(ellipse at 45% 50%,rgba(134,105,63,.07),rgba(134,105,63,0) 70%)"></div>
  <svg class="photo" style="left:116px;top:872px" width="470" height="470" viewBox="0 0 470 470">
    <defs>
      <linearGradient id="aboutPhoto" x1="0" y1="0" x2="1" y2="1">
        <stop offset="0" stop-color="#6d6560"/>
        <stop offset=".5" stop-color="#8d7a68"/>
        <stop offset="1" stop-color="#c9b49c"/>
      </linearGradient>
    </defs>
    <circle cx="229" cy="229" r="219" fill="url(#aboutPhoto)" role="img" aria-label="Photo of a bouquet wrapped in kraft paper held in someone's arms"/>
    <path d="M400 120A232 232 0 1 1 60 80" fill="none" stroke="#86693f" stroke-width="4" stroke-linecap="round"/>
  </svg>
  <div class="abs script" style="left:619px;top:832px;font-size:42px">About Me</div>
  <div class="abs heading" style="left:616px;top:876px;font-size:44px">Hi I’m Atelier</div>
  <div class="bar" style="left:619px;top:930px"></div>
  <p>Lorem ipsum dolor sit amet, consectetur adipiscing elit, sed do eiusmod tempor incididunt ut labore et dolore magna aliqua. Ut enim ad minim veniam, quis nostrud exercitation ullamco laboris nisi ut aliquip ex ea commodo consequat. Duis aute irure dolor in reprehenderit in voluptate velit esse cillum dolore eu fugiat nulla pariatur. Excepteur sint occaecat cupidatat non proident, sunt in culpa qui officia deserunt mollit anim id est laborum. ut perspiciatis unde omnis iste natus error sit voluptatem accusantium doloremque laudantium, totam rem aperiam, eaque ipsa quae ab illo inventore veritatis et quasi architecto beatae vitae dicta sunt explicabo. Nemo enim ipsam voluptatem quia voluptas sit aspernatur aut odit aut fugit, sed quia consequuntur magni dolores eos qui ratione voluptatem sequi nesciunt. Neque porro quisquam est, qui dolorem ipsum quia dolor sit amet, consectetur, adipisci velit, sed quia non numquam eius modi tempora incidunt ut labore.</p>
  <div class="btn" style="left:619px;top:1289px;width:171px;height:46px">Learn More</div>
</section>

<!-- references -->
<section class="refs">
  <svg class="abs" style="left:0;top:1410px" width="1200" height="610" viewBox="0 1410 1200 610" role="img" aria-label="Faded photo of a yellow armchair and a table with flowers">
    <defs>
      <linearGradient id="refTone" x1="0" y1="0" x2="1" y2="0">
        <stop offset="0" stop-color="#ece6d8"/>
        <stop offset=".5" stop-color="#f4f0ea"/>
        <stop offset="1" stop-color="#ece5d3"/>
      </linearGradient>
    </defs>
    <path d="M0 1532Q600 1370 1200 1532V1900Q600 2050 0 1900Z" fill="url(#refTone)"/>
    <path d="M0 1525Q600 1325 1200 1525" fill="none" stroke="#86693f" stroke-width="5"/>
    <path d="M0 1914Q600 2086 1200 1914" fill="none" stroke="#86693f" stroke-width="5"/>
  </svg>
  <div class="abs script" style="left:0;width:1200px;text-align:center;top:1484px;font-size:40px">References</div>
  <div class="abs heading" style="left:0;width:1200px;text-align:center;top:1532px;font-size:44px">Lorem ipsum dolor sit amet</div>
  <div class="bar" style="left:575px;top:1585px"></div>
  <p>Lorem ipsum dolor sit amet, consectetur adipiscing elit, sed do eiusmod tempor incididunt ut labore et dolore magna aliqua. Ut enim ad minim veniam, quis nostrud exercitation ullamco laboris nisi ut aliquip ex ea commodo consequat. Duis aute irure dolor in reprehenderit in voluptate velit esse cillum dolore eu fugiat nulla pariatur. Excepteur sint occaecat cupidatat non proident, sunt in culpa qui officia deserunt mollit anim id est laborum. ut perspiciatis unde omnis iste natus error sit voluptatem accusantium doloremque laudantium, totam rem aperiam, eaque ipsa quae ab illo inventore veritatis et quasi architecto beatae vitae dicta sunt explicabo. Nemo enim ipsam voluptatem quia voluptas sit aspernatur aut odit aut fugit, sed quia consequuntur magni dolores eos qui ratione voluptatem sequi nesciunt. Neque porro quisquam est, qui dolorem ipsum quia dolor sit amet, consectetur, adipisci velit, sed quia non numquam eius modi tempora incidunt ut labor e.quia consequuntur magni dolores eos qui ratione voluptatem sequi nesciunt. Neque porro quisquam est, qui dolorem ipsum quia dolor sit amet, consectetur, adipisci velit, sed quia non numquam eius modi tempora incidunt ut labore et dolore magnam aliquam quaerat voluptatem. Ut enim ad minima veniam, quis nostrum exercitationem ullam corporis suscipit.</p>
  <div class="btn" style="left:514px;top:1856px;width:172px;height:46px">Learn More</div>
</section>

<!-- gallery -->
<section class="gallery">
  <div class="abs script" style="left:0;width:1200px;text-align:center;top:2072px;font-size:40px">Our Gallery</div>
  <div class="abs heading" style="left:0;width:1200px;text-align:center;top:2124px;font-size:42px">Follow Us To Instagram</div>
  <div class="bar" style="left:575px;top:2176px"></div>
  <div class="photo" role="img" aria-label="Photo of a large wildflower bouquet by a wooden wall" style="left:131px;top:2213px;width:226px;height:265px;background:linear-gradient(160deg,#6b4a34,#7d8c5a 55%,#4d3a2c)"></div>
  <div class="photo" role="img" aria-label="Photo of a hanging dried flower installation" style="left:131px;top:2489px;width:226px;height:149px;background:linear-gradient(180deg,#ece9e4,#c08a5a 55%,#e9e6e1)"></div>
  <div class="photo" role="img" aria-label="Photo of a yellow armchair with flowers on a side table" style="left:368px;top:2213px;width:226px;height:150px;background:linear-gradient(120deg,#5c4530,#d4a832 55%,#8f6d3c)"></div>
  <div class="photo" role="img" aria-label="Photo of curly willow and yellow blooms in a dark green vase" style="left:368px;top:2374px;width:226px;height:264px;background:linear-gradient(180deg,#eeecea,#d9d5cd 55%,#4f5a3c 78%,#e8e6e2)"></div>
  <div class="photo" role="img" aria-label="Photo of a single cotton stem in a slim vase" style="left:606px;top:2213px;width:226px;height:265px;background:linear-gradient(180deg,#e4e1de,#d8d3ce 60%,#a58f7c 82%,#e0ddd9)"></div>
  <div class="photo" role="img" aria-label="Photo of green hellebores in a bronze vase" style="left:606px;top:2489px;width:226px;height:149px;background:linear-gradient(180deg,#eeeeec,#b8c69a 40%,#6c4a32 75%,#eceae7)"></div>
  <div class="photo" role="img" aria-label="Photo of daisies and moss inside a glass bowl" style="left:843px;top:2213px;width:226px;height:150px;background:linear-gradient(160deg,#5a6470,#c7cfd1 40%,#6f7d44 70%,#3f4349)"></div>
  <div class="photo" role="img" aria-label="Photo of curly willow and orange blooms in a green vase" style="left:843px;top:2374px;width:226px;height:264px;background:linear-gradient(180deg,#eeecea,#dcd5c9 55%,#5b6645 78%,#e8e6e2)"></div>
</section>

<!-- contact -->
<section class="contact">
  <div class="abs contact-bg" role="img" aria-label="Faded photo of flowers behind the contact area"></div>
  <div class="abs heading" style="left:145px;top:2806px;font-size:42px">Contact Info</div>
  <div class="bar" style="left:145px;top:2860px"></div>
  <svg class="abs" style="left:149px;top:2906px" width="24" height="32" viewBox="0 0 24 32"><path fill="#86693f" d="M12 0C5.4 0 0 5.3 0 11.8 0 20.6 12 32 12 32s12-11.4 12-20.2C24 5.3 18.6 0 12 0zm0 16.5a4.8 4.8 0 1 1 0-9.6 4.8 4.8 0 0 1 0 9.6z"/></svg>
  <div class="info-item" style="top:2906px">123 Lorem ipsum dolor sit amet<br>consectetur adipiscing elit.</div>
  <svg class="abs" style="left:147px;top:2986px" width="28" height="28" viewBox="0 0 24 24"><path fill="#86693f" d="M6.6 10.8a15 15 0 0 0 6.6 6.6l2.2-2.2c.3-.3.7-.4 1-.2 1.1.4 2.3.6 3.6.6.6 0 1 .4 1 1V20c0 .6-.4 1-1 1A17 17 0 0 1 3 4c0-.6.4-1 1-1h3.5c.6 0 1 .4 1 1 0 1.2.2 2.4.6 3.6.1.3 0 .7-.2 1z"/></svg>
  <div class="info-item" style="top:2984px">+1 555 014 2290</div>
  <svg class="abs" style="left:148px;top:3048px" width="26" height="20" viewBox="0 0 24 18"><path fill="#86693f" d="M0 0h24v2L12 10 0 2zM0 4l12 8 12-8v14H0z"/></svg>
  <div class="info-item" style="top:3042px">hello@petalsprite.example</div>
  <span class="social-sq" style="left:147px;background:#3b5998"></span>
  <span class="social-sq" style="left:187px;background:#c13584"></span>
  <span class="social-sq" style="left:227px;background:#e62117"></span>

  <div class="abs heading" style="left:613px;top:2806px;font-size:42px">Get in Touch</div>
  <div class="bar" style="left:615px;top:2860px"></div>
  <div class="field" style="left:614px;top:2908px;width:216px;height:46px">Full Name :</div>
  <div class="field" style="left:837px;top:2908px;width:216px;height:46px">Last Name :</div>
  <div class="field" style="left:614px;top:2961px;width:216px;height:46px">Email:</div>
  <div class="field" style="left:837px;top:2961px;width:216px;height:46px">Phone:</div>
  <div class="field" style="left:614px;top:3019px;width:439px;height:89px">Message:</div>
  <div class="btn" style="left:614px;top:3140px;width:172px;height:47px">Submit</div>
</section>

<!-- footer -->
<footer class="footer">
  <svg class="abs" style="left:0;top:3265px" width="1200" height="441" viewBox="0 3265 1200 441">
    <path d="M0 3380Q600 3190 1200 3380V3706H0Z" fill="#000"/>
    <path d="M0 3368Q600 3178 1200 3368" fill="none" stroke="#86693f" stroke-width="4"/>
  </svg>
  <div class="abs" style="left:186px;top:3420px;width:76px;height:76px;border-radius:50%;border:1px solid #fff"></div>
  <div class="abs" style="left:140px;top:3510px;width:170px;text-align:center;font-size:22px;font-weight:500;color:var(--white)">Petal Sprite</div>

  <h4 style="left:390px">IMPORTANT LINKS</h4>
  <ul>
    <li style="left:390px;top:3428px"><span class="chev">»</span>Home</li>
    <li style="left:390px;top:3456px"><span class="chev">»</span>About Me</li>
    <li style="left:390px;top:3484px"><span class="chev">»</span>Gallery</li>
    <li style="left:390px;top:3512px"><span class="chev">»</span>References</li>
    <li style="left:390px;top:3540px"><span class="chev">»</span>Contact Me</li>
  </ul>
  <h4 style="left:600px">LEGAL</h4>
  <ul>
    <li style="left:600px;top:3428px"><span class="chev">»</span>Privacy Policy</li>
    <li style="left:600px;top:3456px"><span class="chev">»</span>Terms &amp; Conditions</li>
    <li style="left:600px;top:3484px"><span class="chev">»</span>Contact Us</li>
    <li style="left:600px;top:3512px"><span class="chev">»</span>FAQs</li>
  </ul>
  <h4 style="left:824px">CONTACT US</h4>
  <ul>
    <li style="left:824px;top:3428px;line-height:28px">
      <svg width="10" height="13" viewBox="0 0 24 32" style="margin-right:10px"><path fill="#fff" d="M12 0C5.4 0 0 5.3 0 11.8 0 20.6 12 32 12 32s12-11.4 12-20.2C24 5.3 18.6 0 12 0zm0 16.5a4.8 4.8 0 1 1 0-9.6 4.8 4.8 0 0 1 0 9.6z"/></svg>123 Lorem ipsum dolor sit amet<br><span style="padding-left:24px">consectetur adipiscing.</span></li>
    <li style="left:824px;top:3492px">
      <svg width="12" height="12" viewBox="0 0 24 24" style="margin-right:12px"><path fill="#fff" d="M6.6 10.8a15 15 0 0 0 6.6 6.6l2.2-2.2c.3-.3.7-.4 1-.2 1.1.4 2.3.6 3.6.6.6 0 1 .4 1 1V20c0 .6-.4 1-1 1A17 17 0 0 1 3 4c0-.6.4-1 1-1h3.5c.6 0 1 .4 1 1 0 1.2.2 2.4.6 3.6.1.3 0 .7-.2 1z"/></svg>+1 555 014 2290</li>
    <li style="left:824px;top:3532px">
      <svg width="14" height="11" viewBox="0 0 24 18" style="margin-right:10px"><path fill="#fff" d="M0 0h24v2L12 10 0 2zM0 4l12 8 12-8v14H0z"/></svg>hello@petalsprite.example</li>
  </ul>
  <div class="abs foot-line"></div>
  <div class="abs copy">© Copyright 2022&nbsp; Petal Sprite &nbsp;&nbsp; | &nbsp;&nbsp; All Rights Reserved</div>
  <span class="foot-circle" style="left:520px"></span>
  <span class="foot-circle" style="left:564px"></span>
  <span class="foot-circle" style="left:608px"></span>
  <span class="foot-circle" style="left:652px"></span>
</footer>

</body>
</html>
```